Brass Kettle Business Card

I needed some business cards done for my band. We are a 9 piece funk/horn band that plays a lot of private parties, wedding receptions and music festivals. We'd like a design with vivid colors that incorporates our logo. You can check out our website at www.brasskettleband.com to see what type of vibe we are going for.

```html
<!DOCTYPE html>
<html lang="en">
<head>
<meta charset="utf-8">
<title>Brass Kettle Business Card</title>
<link rel="stylesheet" href="https://fonts.googleapis.com/css2?family=Raleway:wght@400;500;700;800&display=swap">
<style>
  :root {
    --lime: #c6e01b;
    --ink: #111111;
    --paper: #ffffff;
    --stage: #3a3a3a;
    --text: #1a1a1a;
  }
  * { box-sizing: border-box; margin: 0; padding: 0; }
  html, body {
    width: 1200px; height: 1200px; overflow: hidden;
    background: var(--stage);
    font-family: "Raleway", sans-serif;
  }
  .sheet {
    width: 1200px; height: 1200px;
    display: flex; flex-direction: column; align-items: center; justify-content: center;
    gap: 60px;
  }
  .card {
    position: relative;
    width: 900px; height: 514px;
    border-radius: 44px;
    overflow: hidden;
    border-bottom: 6px solid var(--lime);
  }
  .card-front { background: var(--paper); }
  .card-back {
    background: radial-gradient(circle at 40% 30%, #222 0%, var(--ink) 70%);
    display: flex; align-items: center; justify-content: center;
  }
  .contact {
    position: absolute; left: 70px; bottom: 70px;
    color: var(--text);
  }
  .contact-name {
    font-weight: 700; font-size: 38px; color: var(--lime);
    letter-spacing: 0.5px; line-height: 1;
  }
  .contact-role {
    font-weight: 500; font-size: 20px; letter-spacing: 1px;
    margin-top: 4px; margin-bottom: 22px;
  }
  .contact-list { list-style: none; }
  .contact-item {
    display: flex; align-items: center; gap: 14px;
    font-size: 24px; font-weight: 500; line-height: 1.55;
  }
  .contact-icon { width: 26px; height: 26px; flex: none; }
  .social { display: flex; align-items: center; gap: 10px; margin-top: 18px; }
  .social-dot {
    width: 30px; height: 30px; border-radius: 50%; background: var(--lime);
  }
  .social-handle { font-size: 24px; font-weight: 500; margin-left: 8px; }
  .brand-lockup {
    position: absolute; right: 70px; top: 110px;
    display: flex; align-items: center; gap: 18px;
  }
  .brand-dot {
    width: 70px; height: 70px; border-radius: 50%; background: var(--lime);
  }
  .brand-name {
    font-weight: 800; font-size: 52px; color: var(--ink);
  }
  .back-name {
    font-weight: 800; font-size: 118px; color: var(--lime);
    letter-spacing: 1px;
  }
</style>
</head>
<body>
<main class="sheet">
  <section class="card card-front" aria-label="Card front">
    <div class="brand-lockup">
      <span class="brand-dot"></span>
      <span class="brand-name">Brass Kettle</span>
    </div>
    <div class="contact">
      <p class="contact-name">FULL NAME</p>
      <p class="contact-role">POSITION</p>
      <ul class="contact-list">
        <li class="contact-item">
          <svg class="contact-icon" viewBox="0 0 24 24"><path fill="var(--lime)" d="M6.6 10.8a15 15 0 0 0 6.6 6.6l2.2-2.2a1 1 0 0 1 1-.25 11.4 11.4 0 0 0 3.6.57 1 1 0 0 1 1 1V20a1 1 0 0 1-1 1A17 17 0 0 1 3 4a1 1 0 0 1 1-1h3.5a1 1 0 0 1 1 1c0 1.25.2 2.45.57 3.57a1 1 0 0 1-.25 1z"/></svg>
          555.014.2290
        </li>
        <li class="contact-item">
          <svg class="contact-icon" viewBox="0 0 24 24"><rect x="2" y="5" width="20" height="14" fill="var(--lime)"/><path d="M2 5l10 8 10-8" fill="none" stroke="#fff" stroke-width="1.6"/></svg>
          info@brasskettleband.com
        </li>
        <li class="contact-item">
          <svg class="contact-icon" viewBox="0 0 24 24" fill="none" stroke="var(--lime)" stroke-width="1.8"><circle cx="12" cy="12" r="10"/><ellipse cx="12" cy="12" rx="4.5" ry="10"/><path d="M2 12h20M4 7h16M4 17h16"/></svg>
          www.brasskettleband.com
        </li>
      </ul>
      <div class="social">
        <span class="social-dot"></span>
        <span class="social-dot"></span>
        <span class="social-dot"></span>
        <span class="social-handle">@brasskettleband</span>
      </div>
    </div>
  </section>

  <section class="card card-back" aria-label="Card back">
    <span class="back-name">Brass Kettle</span>
  </section>
</main>
</body>
</html>
```